Australian IT Company requires Business Card Design

Bluewattle is an Australian company that specialises in IT consulting & support, software development, project management, network services.

We have been in business for 15 years.

* We require a business card with the following on it:
Logo
Address
Contact Details
Space for staff name, title & mobile number

Industry/Entity Type

Software

```html
<!DOCTYPE html>
<html lang="en">
<head>
<meta charset="utf-8">
<title>Bluewattle Business Card</title>
<link rel="stylesheet" href="https://fonts.googleapis.com/css2?family=Open+Sans:wght@400;600&display=swap">
<style>
  :root {
    --brand-blue: #3c6e99;
    --brand-blue-dark: #2f5a80;
    --ink: #1c1c1c;
    --paper: #ffffff;
    --backdrop: #e4e5e7;
  }
  * { box-sizing: border-box; margin: 0; padding: 0; }
  html, body {
    width: 1200px; height: 680px; overflow: hidden;
    background: var(--backdrop);
    font-family: "Open Sans", Arial, sans-serif;
  }
  .stage {
    position: relative; width: 1200px; height: 680px;
    display: flex; align-items: center; justify-content: center; gap: 40px;
  }
  .card {
    position: relative; width: 540px; height: 309px;
    box-shadow: 0 2px 8px rgba(0,0,0,0.12);
  }

  /* Front */
  .card--front { background: var(--paper); }
  .brand {
    position: absolute; left: 40px; top: 46px;
    display: flex; align-items: center; gap: 12px;
  }
  .brand__mark { width: 34px; height: 34px; background: var(--brand-blue); }
  .brand__name {
    font-size: 30px; font-weight: 600; letter-spacing: 0.5px;
    color: var(--brand-blue); line-height: 1;
  }
  .brand__tagline {
    font-size: 9px; letter-spacing: 1px;
    color: var(--brand-blue); margin-top: 5px;
  }
  .header-rule {
    position: absolute; left: 40px; right: 40px; top: 106px;
    border-top: 1.5px solid var(--ink);
  }
  .address {
    position: absolute; right: 40px; top: 120px;
    text-align: right; font-size: 14px; line-height: 1.3; color: var(--ink);
    font-style: normal;
  }
  .staff {
    position: absolute; left: 40px; top: 160px; width: 210px;
    padding-bottom: 6px; border-bottom: 1.5px solid var(--ink);
  }
  .staff__name { font-size: 20px; color: var(--brand-blue); }
  .staff__title { font-size: 13px; color: var(--ink); margin-left: 4px; }
  .contacts {
    position: absolute; left: 40px; top: 200px;
    list-style: none; font-size: 14px; line-height: 1.25; color: var(--ink);
  }
  .contacts li { display: flex; align-items: center; gap: 12px; }
  .contacts svg { width: 14px; height: 14px; fill: var(--brand-blue-dark); flex: none; }
  .card__band {
    position: absolute; left: 0; right: 0; bottom: 0; height: 14px;
    background: var(--brand-blue);
  }

  /* Back */
  .card--back {
    background: var(--brand-blue); color: var(--paper);
    display: flex; flex-direction: column; align-items: center; justify-content: center;
  }
  .card--back .brand { position: static; }
  .card--back .brand__mark { background: var(--paper); width: 44px; height: 44px; }
  .card--back .brand__name { color: var(--paper); font-size: 36px; }
  .card--back .brand__tagline { color: var(--paper); font-size: 11px; letter-spacing: 1px; }
  .back__web {
    margin-top: 44px; font-size: 14px; letter-spacing: 4px;
  }
</style>
</head>
<body>
<main class="stage">
  <section class="card card--front" aria-label="Business card front">
    <div class="brand">
      <span class="brand__mark"></span>
      <div>
        <div class="brand__name">BLUEWATTLE</div>
        <div class="brand__tagline">Technology You Can Rely On</div>
      </div>
    </div>
    <div class="header-rule"></div>
    <address class="address">
      14 Ridge Street<br>Unit Building 3<br>Kelvale Vic 3190
    </address>
    <div class="staff">
      <span class="staff__name">Liam Harwood</span><span class="staff__title">Manager</span>
    </div>
    <ul class="contacts">
      <li><svg viewBox="0 0 16 16"><path d="M3.5 1.5l2.5 0 1 3.5-1.7 1.2a8 8 0 0 0 4.5 4.5l1.2-1.7 3.5 1v2.5c0 .8-.7 1.5-1.5 1.5C6.8 14 2 9.2 2 3c0-.8.7-1.5 1.5-1.5z"/></svg>+61 3 9450 2210</li>
      <li><svg viewBox="0 0 16 16"><path d="M4.5 1h7c.6 0 1 .4 1 1v12c0 .6-.4 1-1 1h-7c-.6 0-1-.4-1-1V2c0-.6.4-1 1-1zm.8 2v8.5h5.4V3zM8 12.5a.8.8 0 1 0 0 1.6.8.8 0 0 0 0-1.6z"/></svg>+61 3 9450 2200</li>
      <li><svg viewBox="0 0 16 16"><path d="M1 3h14v10H1zm1.5 1.2v.4L8 8.6l5.5-4v-.4zm0 2.2v5.4h11V6.4L8 10.4z"/></svg>liam@bluewattle.net.au</li>
      <li><svg viewBox="0 0 16 16"><path d="M8 1a7 7 0 1 0 0 14A7 7 0 0 0 8 1zm-.7 1.6v2.9H5.1c.4-1.5 1.2-2.6 2.2-2.9zm1.4 0c1 .3 1.8 1.4 2.2 2.9H8.7zM4.8 6.9h2.5v2.2H4.8a9 9 0 0 1 0-2.2zm3.9 0h2.5a9 9 0 0 1 0 2.2H8.7zM5.1 10.5h2.2v2.9c-1-.3-1.8-1.4-2.2-2.9zm3.6 0h2.2c-.4 1.5-1.2 2.6-2.2 2.9zM3.4 6.9a9 9 0 0 0 0 2.2H2.5a5.6 5.6 0 0 1 0-2.2zm9.2 0h.9a5.6 5.6 0 0 1 0 2.2h-.9a9 9 0 0 0 0-2.2z"/></svg>www.bluewattle.net.au</li>
    </ul>
    <div class="card__band"></div>
  </section>

  <section class="card card--back" aria-label="Business card back">
    <div class="brand">
      <span class="brand__mark"></span>
      <div>
        <div class="brand__name">BLUEWATTLE</div>
        <div class="brand__tagline">Technology You Can Rely On</div>
      </div>
    </div>
    <div class="back__web">www.bluewattle.net.au</div>
  </section>
</main>
</body>
</html>
```